bizcards, stationary, envelopes, powerpoint template, invoice template, polo shirts, email template
ms word templates of stationary also please
bizcards, stationary, envelopes,  powerpoint template, invoice template, polo shirts, email template - Aviation
Creative Brief
Professional
Samuel K Orlowski
Founder
The Halvern Tower 482 Tamsin Ridge Rd. Suite 210 Fernmoor, OK 44718
sorlowski@meridowair.example
www.meridowair.example
Air Carrier #4RXB519T
Only use the colors and font of our logo. Our tag line "THE SPEED IS YOURS" can be used in a creative way of your thoughts.
wide ope, maybe a Skyvalent Jet watermark, the tag line, the tag line & logo, etc.

```html
<!DOCTYPE html>
<html lang="en">
<head>
<meta charset="utf-8">
<title>Meridow Air — Business Card</title>
<link rel="stylesheet" href="https://fonts.googleapis.com/css2?family=Josefin+Sans:wght@400;600&family=Open+Sans:ital,wght@0,400;0,600;1,800&display=swap">
<style>
  :root {
    --green: #8cc63f;
    --green-dark: #6fa82a;
    --green-pale: #e6f2d6;
    --ink: #3b3b3b;
    --grey: #8a8a8a;
    --paper: #ffffff;
    --backdrop: #eceae6;
    --sky-top: #dfe6ec;
    --sky-bottom: #9aa6b0;
  }
  * { box-sizing: border-box; margin: 0; padding: 0; }
  html, body { width: 1200px; height: 506px; overflow: hidden; }
  body {
    background: var(--backdrop);
    font-family: "Open Sans", Arial, sans-serif;
    position: relative;
  }
  .card {
    position: absolute;
    top: 106px;
    width: 492px;
    height: 300px;
    background: var(--paper);
    overflow: hidden;
    box-shadow: 0 3px 10px rgba(0,0,0,.18);
  }
  .card--front { left: 96px; }
  .card--back { left: 612px; background: var(--green); }

  .card__swoosh { position: absolute; inset: 0; }

  .brand {
    position: absolute;
    left: 28px;
    top: 34px;
    display: flex;
    align-items: center;
    gap: 14px;
  }
  .brand__square { width: 52px; height: 52px; background: var(--green); }
  .brand__name {
    font-family: "Josefin Sans", Arial, sans-serif;
    font-weight: 600;
    font-size: 33px;
    letter-spacing: 6px;
    color: var(--ink);
    padding-top: 6px;
  }

  .address {
    position: absolute;
    left: 96px;
    top: 108px;
    font-size: 10px;
    line-height: 14px;
    color: var(--grey);
  }

  .contacts {
    position: absolute;
    left: 0;
    top: 168px;
    display: grid;
    grid-template-columns: 88px auto;
    font-size: 10px;
    line-height: 15px;
  }
  .contacts dt {
    background: var(--green);
    color: var(--paper);
    padding-left: 28px;
    border-bottom: 1px solid var(--paper);
  }
  .contacts dd { color: var(--grey); padding-left: 8px; }

  .license {
    position: absolute;
    right: 22px;
    bottom: 36px;
    text-align: right;
    font-size: 10px;
    line-height: 14px;
    color: var(--grey);
  }

  .card__field { position: absolute; inset: 0; }
  .back-brand {
    position: absolute;
    left: 24px;
    top: 24px;
  }
  .back-brand__square { display: block; width: 36px; height: 36px; background: var(--green); }
  .jet-visual {
    position: absolute;
    left: 120px;
    top: 30px;
    width: 350px;
    height: 150px;
    border-radius: 50% 40% 45% 50% / 50%;
    background: radial-gradient(ellipse at 55% 45%, var(--sky-top), var(--sky-bottom) 75%, transparent 76%);
  }
  .tagline {
    position: absolute;
    right: 22px;
    bottom: 42px;
    font-style: italic;
    font-weight: 800;
    font-size: 22px;
    color: #2b2b2b;
    letter-spacing: .5px;
  }
  .tagline__accent { color: var(--paper); font-size: 30px; }
</style>
</head>
<body>

<section class="card card--front" aria-label="Business card front">
  <svg class="card__swoosh" viewBox="0 0 492 300" preserveAspectRatio="none" aria-hidden="true">
    <path d="M170 300 C260 200 380 150 492 150 L492 300 Z" fill="var(--green-pale)"/>
    <path d="M230 300 C300 230 400 190 492 180 L492 300 Z" fill="var(--green)" opacity=".55"/>
  </svg>

  <div class="brand">
    <span class="brand__square"></span>
    <span class="brand__name">MERIDOW AIR</span>
  </div>

  <p class="address">The Halvern Tower, 482 Tamsin Ridge Rd.<br>Suite 210 Fernmoor, OK 44718</p>

  <dl class="contacts">
    <dt>Toll free</dt><dd>877-555-0142</dd>
    <dt>Phone</dt><dd>555-555-0187</dd>
    <dt>Cell</dt><dd>555-555-0163</dd>
    <dt>Fax</dt><dd>555-555-0129</dd>
    <dt>Email</dt><dd>sorlowski@meridowair.example</dd>
  </dl>

  <p class="license">License No., if any<br>Air Carrier #4RXB519T</p>
</section>

<section class="card card--back" aria-label="Business card back">
  <svg class="card__field" viewBox="0 0 492 300" preserveAspectRatio="none" aria-hidden="true">
    <path d="M0 0 L492 0 L492 190 C380 215 250 210 0 150 Z" fill="var(--paper)"/>
  </svg>
  <div class="back-brand">
    <span class="back-brand__square"></span>
  </div>
  <div class="jet-visual" role="img" aria-label="Photograph of a private business jet in flight"></div>
  <p class="tagline">THE <span class="tagline__accent">SPEED</span> IS YOURS</p>
</section>

</body>
</html>
```